Every sort of trades everysortoftrades.ca

Website for company offering Every sort of trades
Welding/Fabrication/Metal repairs/Metal building, Electrical repairs and installations, Plumbing and Heating, Renovations, Flooring, Paiting, and other services

We need a very clean and professional website outlining the many services we have

We would like each type of service to have its own page, with images of those types of services on those pages.

Then in the future, we can update those pages with projects we have done of those types.

Every Sort of Trades . CA

Located in Calgary, Alberta, Canada, offering services Alberta wide

Welding/Fabrication/Repair/Building - Steel and metals
Electrical contractor - Journeyman , small or large projects
Plumbing and Heating
Renovations
Flooring
Painting
Other services - storage, trucking, delivery, etc

business and residential services

Contractor

5+ page

Sans Serif

3176b5
0253a1
85acd3
85abd2
cedeed
ffffff

Must have
• Clean
• Professional
• Easy of updating text and images

```html
<!DOCTYPE html>
<html lang="en">
<head>
<meta charset="utf-8">
<title>Every sort of trades</title>
<link rel="stylesheet" href="https://fonts.googleapis.com/css2?family=Lato:wght@300;400;700;900&family=Open+Sans:wght@400;600;700&family=Raleway:wght@400;500;600;700&display=swap">
<style>
:root{
  --blue:#3176b5;
  --navy:#0253a1;
  --sky:#85acd3;
  --pale:#cedeed;
  --white:#ffffff;
  --ink:#222222;
  --text:#555555;
  --muted:#8a8a8a;
  --offwhite:#f6f6f6;
  --footer:#232323;
  --footer-deep:#1b1b1b;
}
*{box-sizing:border-box;margin:0;padding:0}
html,body{width:1200px;height:2647px;overflow:hidden}
body{position:relative;background:var(--white);font-family:"Open Sans",Arial,sans-serif;color:var(--text)}
.abs{position:absolute}

/* header */
.topline{left:0;top:0;width:1200px;height:5px;background:var(--navy)}
.header{left:0;top:5px;width:1200px;height:110px;background:var(--white)}
.brand{left:127px;top:30px;display:flex;align-items:center;gap:12px}
.brand-mark{width:34px;height:34px;background:var(--navy)}
.brand-name{font-family:"Lato",sans-serif;font-weight:900;font-size:25px;color:var(--navy);line-height:1}
.nav{left:0;top:54px;width:1200px;height:16px;font-family:"Raleway",sans-serif;font-size:11.5px;color:#444;text-transform:uppercase;letter-spacing:.2px}
.nav span{position:absolute;top:0;white-space:nowrap}
.search{left:1066px;top:51px}

/* info bar */
.infobar{left:0;top:115px;width:1200px;height:85px;background:var(--pale)}
.info{display:flex;gap:12px;align-items:flex-start}
.info h4{font-family:"Raleway",sans-serif;font-weight:700;font-size:17px;color:#1d2b3a;margin-bottom:3px}
.info p{font-size:12px;color:#2f3b48;line-height:1.3}

/* hero */
.hero{left:0;top:200px;width:1200px;height:562px;background:linear-gradient(90deg,#0b4c9c 0%,#1c5ea8 38%,#5a7ea6 65%,#8a98a6 100%)}
.hero-kicker{left:127px;top:342px;font-family:"Lato",sans-serif;font-weight:300;font-size:28px;color:var(--white);letter-spacing:1.5px}
.hero-rule{left:127px;top:389px;width:365px;height:1px;background:rgba(255,255,255,.6)}
.hero-title{left:123px;top:406px;font-family:"Lato",sans-serif;font-weight:900;font-size:39.5px;line-height:48px;color:var(--white)}
.hero-btn{left:125px;top:526px;width:152px;height:44px;background:var(--pale);transform:skewX(-16deg)}
.hero-btn span{display:block;transform:skewX(16deg);text-align:center;line-height:44px;font-family:"Lato",sans-serif;font-size:15px;color:#1d2b3a}

/* about */
.about-title{left:105px;top:915px;font-family:"Lato",sans-serif;font-weight:400;font-size:33.5px;color:#2a2a2a;letter-spacing:.3px}
.about-text{left:107px;top:972px;width:490px;font-size:12px;line-height:19px;color:#333}
.about-text p{margin-bottom:19px}
.about-photo{left:635px;top:866px;width:397px;height:380px;background:linear-gradient(180deg,#f2f2f2 0%,#d9c27a 35%,#3e5a86 75%,#2e3f5c 100%);border-radius:120px 120px 0 0}

/* services */
.services{left:0;top:1246px;width:1200px;height:531px;background:linear-gradient(160deg,#0a58a6 0%,var(--navy) 55%,#02498e 100%)}
.services-title{left:0;top:1297px;width:1200px;text-align:center;font-family:"Lato",sans-serif;font-weight:400;font-size:46px;color:var(--white)}
.service-card{top:1435px;width:305px;height:247px}
.service-photo{position:absolute;left:0;top:0;width:305px;height:199px}
.service-label{position:absolute;left:0;top:199px;width:305px;height:48px;background:var(--blue)}
.service-label span{position:absolute;left:0;width:305px;padding-left:80px;top:0;line-height:48px;text-align:center;font-family:"Lato",sans-serif;font-size:21px;color:var(--white);letter-spacing:.5px}
.service-hex{position:absolute;left:26px;top:178px}

/* offers */
.offers{left:0;top:1777px;width:1200px;height:505px;background:var(--offwhite)}
.offers-title{left:129px;top:1866px;font-family:"Raleway",sans-serif;font-weight:700;font-size:20px;color:#1e1e1e}
.offers-rule{left:129px;top:1905px;width:43px;height:3px;background:var(--blue)}
.tabs{left:130px;top:1948px;width:231px;list-style:none;background:var(--white)}
.tabs li{height:39.5px;line-height:38px;padding-left:20px;font-size:12.5px;color:#444;border:1px solid #e3e3e3;border-top:none}
.tabs li:first-child{border-top:1px solid #e3e3e3;border-left:4px solid var(--blue);padding-left:17px;color:var(--navy)}
.offers-text{left:386px;top:1947px;width:490px;font-size:12.6px;line-height:21px;color:#6b6b6b}
.offers-photo{left:386px;top:2072px;width:244px;height:143px;background:linear-gradient(135deg,#c79c63 0%,#e7dccb 45%,#5f5a55 100%)}
.ticks{left:656px;top:2078px;list-style:none}
.ticks li{display:flex;align-items:center;gap:12px;height:30px;font-size:12.5px;color:#7a7a7a}
.offers-worker{left:893px;top:1867px;width:175px;height:415px;background:linear-gradient(180deg,#f2d443 0%,#2c3c63 30%,#d8b88a 55%,#2c4f8b 100%);border-radius:60px 60px 0 0}

/* footer */
.footer{left:0;top:2282px;width:1200px;height:330px;background:var(--footer)}
.footer-brand{left:99px;top:2340px;font-family:"Lato",sans-serif;font-weight:900;font-size:24px;color:var(--white)}
.footer-about{left:99px;top:2410px;width:205px;font-size:11.3px;line-height:19px;color:#9a9a9a}
.socials{left:99px;top:2502px;display:flex;gap:8px}
.socials span{width:30px;height:30px;border-radius:50%;background:#555}
.footer-head{top:2317px;font-family:"Raleway",sans-serif;font-weight:700;font-size:13px;color:var(--white);letter-spacing:.5px}
.contact-list{left:357px;top:2360px;list-style:none;font-size:11px;color:#aaa}
.contact-list li{display:flex;gap:10px;line-height:17px;margin-bottom:11px;width:215px}
.contact-list svg{flex:none;margin-top:2px}
.links{left:614px;top:2364px;list-style:none;font-family:"Raleway",sans-serif;font-weight:600;font-size:11px;color:#ddd;text-transform:uppercase}
.links li{height:31.5px}
.links li::before{content:"›";color:var(--blue);margin-right:12px}
.news-text{left:872px;top:2362px;width:232px;font-size:12px;line-height:24px;color:#9a9a9a}
.news-input{left:872px;top:2447px;width:231px;height:42px;border:1px solid #444;padding-left:18px;line-height:40px;font-size:12px;color:#bbb}
.news-btn{left:872px;top:2506px;width:231px;height:43px;background:var(--blue);text-align:center;line-height:43px;font-weight:600;font-size:13px;color:var(--white)}
.copyright{left:0;top:2612px;width:1200px;height:35px;background:var(--footer-deep);text-align:center;line-height:35px;font-size:11px;color:#cfcfcf}
</style>
</head>
<body>

<div class="abs topline"></div>
<header class="abs header"></header>
<div class="abs brand"><span class="brand-mark"></span><span class="brand-name">Every sort of trades</span></div>
<nav class="abs nav">
  <span style="left:467px">Home</span>
  <span style="left:536px">About</span>
  <span style="left:609px">Who are you</span>
  <span style="left:723px">Service</span>
  <span style="left:803px">Our work</span>
  <span style="left:900px">News</span>
  <span style="left:967px">Contact us</span>
</nav>
<svg class="abs search" width="22" height="22" viewBox="0 0 22 22"><circle cx="9" cy="9" r="7" fill="none" stroke="#111" stroke-width="2.5"/><line x1="14" y1="14" x2="20" y2="20" stroke="#111" stroke-width="2.8" stroke-linecap="round"/></svg>

<section class="abs infobar"></section>
<div class="abs info" style="left:133px;top:128px">
  <svg width="28" height="44" viewBox="0 0 28 44"><path d="M14 1C6.8 1 1 6.8 1 14c0 10 13 28 13 28s13-18 13-28C27 6.8 21.2 1 14 1z" fill="var(--navy)"/><circle cx="14" cy="14" r="5" fill="var(--pale)"/></svg>
  <div><h4>Address</h4><p>2210 Bow Trail SW, Suite 140<br>Calgary</p></div>
</div>
<div class="abs info" style="left:472px;top:136px">
  <svg width="38" height="38" viewBox="0 0 38 38"><circle cx="19" cy="19" r="17" fill="none" stroke="var(--navy)" stroke-width="2"/><path d="M13 11c1-1 2.5-1 3 .3l1.3 3c.3.8 0 1.5-.7 2l-1.2.9c.9 2.2 2.5 3.8 4.7 4.7l.9-1.2c.5-.7 1.2-1 2-.7l3 1.3c1.3.5 1.3 2 .3 3l-1.6 1.6c-5.5.4-13.4-7.5-13-13z" fill="var(--navy)"/></svg>
  <div><h4>Call Us</h4><p>(403) 555-0182</p></div>
</div>
<div class="abs info" style="left:831px;top:136px">
  <svg width="38" height="38" viewBox="0 0 38 38"><circle cx="19" cy="19" r="17" fill="none" stroke="var(--navy)" stroke-width="2"/><rect x="10" y="13" width="18" height="13" fill="none" stroke="var(--navy)" stroke-width="2"/><path d="M10 13l9 7 9-7" fill="none" stroke="var(--navy)" stroke-width="2"/></svg>
  <div><h4>Email Address</h4><p>info@everysortoftrades.ca</p></div>
</div>

<section class="abs hero" role="img" aria-label="Photo of a construction worker holding a white hard hat, with a hammer in his belt, under a blue tint"></section>
<div class="abs hero-kicker">EVERY SORT OF TRADES</div>
<div class="abs hero-rule"></div>
<h1 class="abs hero-title">Welding/Fabrication/Repair/Building<br>Steel &amp; metals</h1>
<div class="abs hero-btn"><span>More Details</span></div>

<h2 class="abs about-title">WANT TO KNOW ABOUT US?</h2>
<div class="abs about-text">
  <p>At vero eos et accusamus et iusto odio dignissimos ducimus qui blanditiis praesentium voluptatum deleniti atque corrupti quos dolores et quas molestias excepturi sint occaecati cupiditate non provident.</p>
  <p>Similique sunt in culpa qui officia deserunt mollitia animi, id est laborum et dolorum fuga. Et harum quidem rerum facilis est et expedita distinctio. Nam libero tempore, cum solutanobis.</p>
  <p>Deleniti atque corrupti quos dolores et quas molestias excepturi<br>Sint occaecati cupiditate non provident, similique sunt in<br>Culpa qui officia deserunt mollitia animi, id est laborum et dolorum fuga.</p>
</div>
<div class="abs about-photo" role="img" aria-label="Photo of four tradesmen in yellow hard hats and tool belts"></div>

<section class="abs services"></section>
<h2 class="abs services-title">Our Services</h2>

<div class="abs service-card" style="left:97px">
  <div class="service-photo" role="img" aria-label="Photo of a welder in a mask with sparks" style="background:linear-gradient(135deg,#1e1e22 0%,#3a3c42 50%,#c9762a 80%,#2a2a2e 100%)"></div>
  <div class="service-label"><span>WELDING</span></div>
  <svg class="service-hex" width="62" height="70" viewBox="0 0 62 70"><polygon points="31,2 60,18 60,52 31,68 2,52 2,18" fill="var(--pale)"/><circle cx="31" cy="35" r="10" fill="none" stroke="#222" stroke-width="3"/></svg>
</div>
<div class="abs service-card" style="left:445px">
  <div class="service-photo" role="img" aria-label="Photo of a grinding disc throwing orange sparks" style="background:radial-gradient(circle at 40% 50%,#f7c46a 0%,#d06a1f 30%,#3b2416 75%,#1c1410 100%)"></div>
  <div class="service-label"><span>FABRICATION</span></div>
  <svg class="service-hex" width="62" height="70" viewBox="0 0 62 70"><polygon points="31,2 60,18 60,52 31,68 2,52 2,18" fill="var(--pale)"/><circle cx="31" cy="35" r="10" fill="none" stroke="#222" stroke-width="3"/></svg>
</div>
<div class="abs service-card" style="left:794px">
  <div class="service-photo" role="img" aria-label="Photo of a concrete building under construction against a blue sky" style="background:linear-gradient(180deg,#5f9fe0 0%,#9fc5ea 40%,#b9aa92 70%,#7d705f 100%)"></div>
  <div class="service-label"><span>BUILDING</span></div>
  <svg class="service-hex" width="62" height="70" viewBox="0 0 62 70"><polygon points="31,2 60,18 60,52 31,68 2,52 2,18" fill="var(--pale)"/><rect x="21" y="25" width="20" height="20" fill="#222"/></svg>
</div>

<section class="abs offers"></section>
<h3 class="abs offers-title">Services That We Offers</h3>
<div class="abs offers-rule"></div>
<ul class="abs tabs">
  <li>Electrical contractor</li>
  <li>Plumbing and Heating</li>
  <li>Renovations</li>
  <li>Flooring</li>
  <li>Painting</li>
  <li>Steel and metals</li>
  <li>Other services</li>
</ul>
<p class="abs offers-text">Sed ut perspiciatis unde omnis iste natus error sit voluptatem accusantium doloremque laudantium, totam rem aperiam, eaque ipsa quae ab illo invent ore veritatis et quasi architecto beatae vitae dict eaque ipsa quae ab illo inventore veritatis et quasi architecto.</p>
<div class="abs offers-photo" role="img" aria-label="Photo of hands over a clipboard with a level, calculator and phone on a desk"></div>
<ul class="abs ticks">
  <li><svg width="12" height="12" viewBox="0 0 12 12"><circle cx="6" cy="6" r="5" fill="none" stroke="var(--blue)" stroke-width="1.5"/><path d="M3.5 6l2 2 3-3.5" fill="none" stroke="var(--blue)" stroke-width="1.5"/></svg>Natus erroroluptatem</li>
  <li><svg width="12" height="12" viewBox="0 0 12 12"><circle cx="6" cy="6" r="5" fill="none" stroke="var(--blue)" stroke-width="1.5"/><path d="M3.5 6l2 2 3-3.5" fill="none" stroke="var(--blue)" stroke-width="1.5"/></svg>Accusantium doloremue</li>
  <li><svg width="12" height="12" viewBox="0 0 12 12"><circle cx="6" cy="6" r="5" fill="none" stroke="var(--blue)" stroke-width="1.5"/><path d="M3.5 6l2 2 3-3.5" fill="none" stroke="var(--blue)" stroke-width="1.5"/></svg>Laudantium unde</li>
  <li><svg width="12" height="12" viewBox="0 0 12 12"><circle cx="6" cy="6" r="5" fill="none" stroke="var(--blue)" stroke-width="1.5"/><path d="M3.5 6l2 2 3-3.5" fill="none" stroke="var(--blue)" stroke-width="1.5"/></svg>Natus error sit volupta</li>
  <li><svg width="12" height="12" viewBox="0 0 12 12"><circle cx="6" cy="6" r="5" fill="none" stroke="var(--blue)" stroke-width="1.5"/><path d="M3.5 6l2 2 3-3.5" fill="none" stroke="var(--blue)" stroke-width="1.5"/></svg>Accusantium dolor</li>
</ul>
<div class="abs offers-worker" role="img" aria-label="Photo of a tradesman in a hard hat leaning on a wooden plank"></div>

<footer class="abs footer"></footer>
<div class="abs footer-brand">Every sort of trades</div>
<p class="abs footer-about">Every sort of trades is a registered builder and member of the Prairie Region Home Builders Association.</p>
<div class="abs socials"><span></span><span></span><span></span><span></span></div>

<h4 class="abs footer-head" style="left:357px">GET IN TOUCH</h4>
<ul class="abs contact-list">
  <li><svg width="10" height="12" viewBox="0 0 10 12"><path d="M5 0C2.2 0 0 2.2 0 5c0 3.5 5 7 5 7s5-3.5 5-7c0-2.8-2.2-5-5-5z" fill="var(--blue)"/></svg>815 Macleod Trail SE, Calgary, AB T2G 2M6, Canada</li>
  <li><svg width="10" height="10" viewBox="0 0 10 10"><path d="M1 1.5C1.5 1 2.3 1 2.6 1.6l.8 1.6c.2.4 0 .8-.3 1l-.6.5c.5 1.1 1.3 1.9 2.4 2.4l.5-.6c.3-.3.7-.5 1-.3l1.6.8c.6.3.6 1.1.1 1.6L7.2 9.5C4.4 9.7.3 5.6.5 2.8z" fill="var(--blue)"/></svg>(403) 555-0147</li>
  <li><svg width="10" height="10" viewBox="0 0 10 10"><path d="M0 4.5L10 0 7 10 5 6z" fill="var(--blue)"/></svg>info@everysortoftrades.ca</li>
  <li><svg width="10" height="12" viewBox="0 0 10 12"><rect x="1.5" y="0.5" width="7" height="11" rx="1" fill="none" stroke="var(--blue)" stroke-width="1.2"/></svg>(403) 555-0147</li>
  <li><svg width="10" height="10" viewBox="0 0 10 10"><circle cx="5" cy="5" r="4.3" fill="none" stroke="var(--blue)" stroke-width="1.2"/><path d="M5 2.5V5l1.7 1" fill="none" stroke="var(--blue)" stroke-width="1.2"/></svg>Mon - Sat: 9:00 - 18:00</li>
</ul>

<h4 class="abs footer-head" style="left:614px">INFORMATION</h4>
<ul class="abs links"><li>Home</li><li>Our story</li><li>Our people</li><li>What we do</li><li>Contact us</li></ul>

<h4 class="abs footer-head" style="left:872px">NEWS LETTER</h4>
<p class="abs news-text">Enter your email address for our mailing list to keep your self our lastest updated.</p>
<div class="abs news-input">Email</div>
<div class="abs news-btn">Sign up</div>

<div class="abs copyright">Copyright © 2007 - 2017 Every Sort of Trades.  All Rights Reserved</div>

</body>
</html>
```